I'm an electrician and the name of my company is called Brisk 'N' Bright Electrical. I require a professional business card that speaks to my clients, I also need it to be innovative and modern. We do maintenance & service work for domestic and commercial premises.

Industry/Entity Type

Electrical

Contact Information for Business Card

Must have the name of my company Brisk 'N' Bright Electrical, my name Darren Kolovos and my contact details 0427 381 592 and company email address Brisknbrightelectrical@mailvane.com and/or website Brisknbrightelectrical.com.au

Logo Text

Brisk 'N' Bright Electrical (If possible)

Colors
33a6d7
0592cd
3176b5

```html
<!DOCTYPE html>
<html lang="en">
<head>
<meta charset="utf-8">
<title>Brisk 'N' Bright Electrical – Business Card</title>
<link rel="stylesheet" href="https://fonts.googleapis.com/css2?family=Arimo:wght@400;700&display=swap">
<style>
  :root {
    --page-bg: #e4e6ea;
    --front-top: #7090c6;
    --front-bottom: #2f5191;
    --back-bg: #f1f1f3;
    --wave-blue: #4a6aa8;
    --ink-dark: #1e1f24;
    --ink-light: #ffffff;
    --card-shadow: rgba(20, 30, 50, 0.28);
  }
  * { margin: 0; padding: 0; box-sizing: border-box; }
  html, body {
    width: 1200px;
    height: 855px;
    overflow: hidden;
    background: var(--page-bg);
    font-family: "Arimo", Arial, sans-serif;
  }
  .stage {
    position: relative;
    width: 1200px;
    height: 855px;
  }
  .card {
    position: absolute;
    top: 279px;
    width: 520px;
    height: 297px;
    border-radius: 8px;
    overflow: hidden;
    box-shadow: 0 12px 28px var(--card-shadow);
  }
  .card--front {
    left: 50px;
    background: linear-gradient(180deg, var(--front-top) 0%, var(--front-bottom) 100%);
    display: flex;
    align-items: center;
    justify-content: center;
  }
  .card--back {
    left: 630px;
    background: var(--back-bg);
  }
  .brand {
    display: flex;
    align-items: center;
    gap: 12px;
    font-weight: 700;
    font-size: 36px;
    letter-spacing: 0.5px;
  }
  .brand__dot {
    width: 22px;
    height: 22px;
    border-radius: 50%;
    background: currentColor;
  }
  .card--front .brand { color: var(--ink-light); }
  .card--back .brand {
    position: absolute;
    left: 46px;
    top: 70px;
    color: var(--ink-dark);
    font-size: 32px;
  }
  .holder-name {
    position: absolute;
    right: 36px;
    top: 128px;
    font-weight: 700;
    font-size: 17px;
    color: var(--ink-dark);
    letter-spacing: 0.4px;
    word-spacing: 3px;
  }
  .wave {
    position: absolute;
    left: 0;
    top: 0;
    width: 520px;
    height: 297px;
  }
  .contact {
    position: absolute;
    right: 22px;
    top: 168px;
    list-style: none;
    color: var(--ink-light);
    font-size: 12.5px;
    text-align: right;
  }
  .contact__item {
    display: flex;
    align-items: center;
    justify-content: flex-end;
    gap: 8px;
    height: 21px;
  }
  .contact__item svg { width: 12px; height: 12px; flex: none; }
</style>
</head>
<body>
<main class="stage">
  <section class="card card--front" aria-label="Card front">
    <div class="brand"><span class="brand__dot"></span>Brisk 'N' Bright</div>
  </section>

  <section class="card card--back" aria-label="Card back">
    <svg class="wave" viewBox="0 0 520 297" aria-hidden="true">
      <path d="M0 297 L0 292 C140 285 210 215 300 175 C390 138 460 128 520 150 L520 297 Z" fill="var(--wave-blue)"/>
    </svg>
    <div class="brand"><span class="brand__dot"></span>Brisk 'N' Bright</div>
    <p class="holder-name">Darren Kolovos</p>
    <ul class="contact">
      <li class="contact__item">0427 381 592
        <svg viewBox="0 0 12 12" aria-hidden="true"><rect x="3" y="0.5" width="6" height="11" rx="1" fill="none" stroke="#fff" stroke-width="1"/><circle cx="6" cy="9.8" r="0.6" fill="#fff"/></svg>
      </li>
      <li class="contact__item">Brisknbrightelectrical.com.au
        <svg viewBox="0 0 12 12" aria-hidden="true"><circle cx="6" cy="6" r="5.2" fill="none" stroke="#fff" stroke-width="1"/><ellipse cx="6" cy="6" rx="2.2" ry="5.2" fill="none" stroke="#fff" stroke-width="0.8"/><line x1="0.8" y1="6" x2="11.2" y2="6" stroke="#fff" stroke-width="0.8"/></svg>
      </li>
      <li class="contact__item">Brisknbrightelectrical@mailvane.com
        <svg viewBox="0 0 12 12" aria-hidden="true"><rect x="0.5" y="2.5" width="11" height="7" fill="#fff"/><path d="M0.5 2.5 L6 6.8 L11.5 2.5" fill="none" stroke="var(--wave-blue)" stroke-width="0.9"/></svg>
      </li>
    </ul>
  </section>
</main>
</body>
</html>
```